UPDATED BRIEF: Hypermobile EDS Book Cover Contest

I am writing a print book. I need cover designs to evaluate with your creativity. It is a nonfiction memoir meets self-help guide to living with a rare, incurable chronic illness called EDS. See attached Word doc for book details and copy. It is designed to be an inspiration story of living well with this disease so mindset is a key theme. I'm looking for all types of ideas including photography (sailboat, mountain, journey concepts), type flat designs highlighting hypermobility (a key part of the disease), including good use of color and white space. I want it to be legible, intriguing, and emotive if possible. I need someone to be able to produce and provide the production files and/or edit the final text back copy as it is not yet final. I will be sharing the contest with my fan base. I will ultimately need the cover, back cover, spine, and audio and ebook covers done all the same just reformatted to size. Print book 6x9 to be done first. I dont want to provide too much direction so you can be creative.
Updates

I uploaded a new brief for updated author name and back cover. Please update and I will start the poll. I will also extend the project timeline.

Can anyone create a design with the typeset words of hypermobile on the title being "pinched" by a string? Like holding it all together by a string?

Went on vacation/holiday

Target Market(s)

chronic illness disease victims, specifically those with Hypermobile Ehlers Danlos Syndrome (EDS), dysautonomia (POTS) or craniocervical instability in the neck

Industry/Entity Type

Self help, personal development, memoir

Font styles to use
Sans Serif

Colors
FFC000
F8CF3A
FAE287
FDF2CF
FEFAEE

Requirements
Must have
• legible, intriguing even emotive design with text or photos
Nice to have
• Potentially visually showing a journey, hypermobility, or overcoming obstacles
Should not have
• black dark backgrounds

```html
<!DOCTYPE html>
<html lang="en">
<head>
<meta charset="utf-8">
<title>Keeping It All Aligned When You're Overflexible — Book Cover</title>
<link rel="stylesheet" href="https://fonts.googleapis.com/css2?family=Open+Sans:ital,wght@0,600;0,700;1,500&display=swap">
<style>
  :root {
    --backdrop: #ebebeb;
    --paper: #ffffff;
    --ink-dark: #3b3b3b;
    --ink-black: #0d0d0d;
    --ink-muted: #4a4a4a;
    --accent-yellow: #FFC000;
    --art-light: #f2f2f2;
    --art-mid: #9a9a9a;
    --art-dark: #2a2a2a;
  }
  * { margin: 0; padding: 0; box-sizing: border-box; }
  html, body {
    width: 1200px;
    height: 1200px;
    overflow: hidden;
    background: var(--backdrop);
    font-family: "Open Sans", Arial, sans-serif;
  }
  .book-cover {
    position: absolute;
    left: 240px;
    top: 60px;
    width: 720px;
    height: 1080px;
    background: var(--paper);
  }
  .title-line {
    position: absolute;
    left: 0;
    width: 100%;
    text-align: center;
    font-weight: 700;
    line-height: 1;
    letter-spacing: -0.5px;
    white-space: nowrap;
  }
  .title-line--small-dark { top: 99px; font-size: 57px; color: var(--ink-dark); }
  .title-line--large-dark { top: 166px; font-size: 76px; color: var(--ink-dark); letter-spacing: -1.5px; }
  .title-line--small-yellow { top: 263px; font-size: 57px; color: var(--accent-yellow); }
  .title-line--large-yellow { top: 330px; font-size: 76px; color: var(--accent-yellow); letter-spacing: -1px; }
  .subtitle {
    position: absolute;
    left: 0;
    top: 423px;
    width: 100%;
    text-align: center;
    font-style: italic;
    font-weight: 500;
    font-size: 24px;
    line-height: 30px;
    color: var(--ink-muted);
    letter-spacing: -0.3px;
  }
  .cover-art {
    position: absolute;
    left: 177px;
    top: 537px;
    width: 366px;
    height: 404px;
    display: block;
  }
  .author-name {
    position: absolute;
    left: 0;
    top: 992px;
    width: 100%;
    text-align: center;
    font-weight: 600;
    font-size: 46px;
    line-height: 1;
    color: var(--ink-black);
    letter-spacing: -0.5px;
  }
</style>
</head>
<body>
  <main class="book-cover">
    <h1 class="book-title">
      <span class="title-line title-line--small-dark">KEEPING IT</span>
      <span class="title-line title-line--large-dark">ALL ALIGNED</span>
      <span class="title-line title-line--small-yellow">WHEN YOU’RE</span>
      <span class="title-line title-line--large-yellow">OVERFLEXIBLE</span>
    </h1>
    <p class="subtitle">FIND A STEADIER DAILY RHYTHM WITH<br>LAX JOINTS, DIZZINESS, AND FATIGUE</p>
    <svg class="cover-art" role="img" aria-label="Illustration of a zebra-striped elephant walking toward the viewer" viewBox="0 0 366 404">
      <defs>
        <radialGradient id="artTone" cx="50%" cy="45%" r="60%">
          <stop offset="0%" stop-color="var(--art-mid)"/>
          <stop offset="60%" stop-color="var(--art-dark)" stop-opacity="0.55"/>
          <stop offset="100%" stop-color="var(--art-light)" stop-opacity="0"/>
        </radialGradient>
      </defs>
      <rect x="0" y="0" width="366" height="404" fill="url(#artTone)"/>
    </svg>
    <p class="author-name">MARLA J. BENNING</p>
  </main>
</body>
</html>
```